Design a book cover to attract readers! cover art!

I am looking for a design of a book cover. The working title of the book is: The Sideline Launch: Growing a Venture Around Your Day Job Author R. K. Holloway .....while the book is about balancing work, life, and building a parttime startup, it is also about how to make sure you can give the "F You" to your boss. Following this book will help you get that confidence, freedom, and surety that you are ok if you ever choose to leave your job, and make your part time startup full time.As a result, I'm looking for something catchy, funny, and not 'bland' I'm ok with raunchy, and silly - the book iself is supposed to be a FUN way to learn this; not be the bland and normal 'self help' book.

Target Market(s)

young career (21-28) as well as college/pre college (18-25)

Colors

Designer to choose colors to be used in the design.

Requirements
Must have
• -a spot for the ISBN number (bottom right back of the book)
• -back cover & front cover and a half inch edge cover
• -bottom left will have my company logo (Marlow Group) which you can add into the mockup if you'd like
Nice to have
• something funny/catching
• book expected size 6" by 9"

```html
<!DOCTYPE html>
<html lang="en">
<head>
<meta charset="utf-8">
<title>The Sideline Launch – Cover Spread</title>
<link href="https://fonts.googleapis.com/css2?family=Oswald:wght@700&family=Archivo+Black&family=Arimo:wght@400;700&display=swap" rel="stylesheet">
<style>
  :root {
    --paper: #ffffff;
    --back-teal: #234556;
    --spine-black: #0b0b0c;
    --title-yellow: #fff200;
    --text-white: #ffffff;
    --ink: #111111;
    --cyan: #00aeef;
    --magenta: #ec008c;
    --yellow: #fff200;
    --black: #000000;
  }
  * { margin: 0; padding: 0; box-sizing: border-box; }
  html, body { width: 1200px; height: 900px; overflow: hidden; background: var(--paper); }
  .sheet { position: relative; width: 1200px; height: 900px; background: var(--paper); font-family: "Arimo", Arial, sans-serif; }

  .color-bar { position: absolute; left: 105px; top: 24px; font-size: 10px; letter-spacing: 0.2px; font-family: "Arimo", Arial, sans-serif; }
  .color-bar .c { color: var(--cyan); }
  .color-bar .m { color: var(--magenta); }
  .color-bar .y { color: var(--yellow); }
  .color-bar .k { color: var(--black); }

  .trim-marks, .reg-marks { position: absolute; inset: 0; pointer-events: none; }

  .back-cover { position: absolute; left: 57px; top: 57px; width: 522px; height: 785px; background: var(--back-teal); }
  .publisher-mark { position: absolute; left: 209px; top: 655px; display: flex; align-items: center; gap: 6px; color: var(--text-white); font-family: "Arimo", Arial, sans-serif; font-weight: 700; font-size: 13px; letter-spacing: 3px; white-space: nowrap; }
  .publisher-mark .dot { width: 10px; height: 10px; background: var(--text-white); }
  .isbn-box { position: absolute; left: 338px; top: 720px; width: 156px; height: 26px; background: var(--paper); color: var(--ink); font-weight: 700; font-size: 14px; line-height: 26px; padding-left: 5px; }

  .spine { position: absolute; left: 579px; top: 57px; width: 42px; height: 785px; background: var(--spine-black); overflow: hidden; }
  .spine-text { position: absolute; width: 785px; height: 42px; left: -371.5px; top: 371.5px; transform: rotate(-90deg); display: flex; align-items: center; padding: 0 30px 0 53px; white-space: nowrap; }
  .spine-title { font-family: "Archivo Black", "Arial Black", sans-serif; color: var(--title-yellow); font-size: 22px; }
  .spine-subtitle { margin-left: 10px; color: var(--text-white); font-weight: 700; font-size: 10.5px; }
  .spine-author { margin-left: auto; color: var(--text-white); font-weight: 700; font-size: 9.5px; }

  .front-cover { position: absolute; left: 621px; top: 57px; width: 522px; height: 785px;
    background: radial-gradient(ellipse 75% 70% at 56% 72%, #a3d0dc 0%, #5e9db3 22%, #2d6882 42%, #173647 62%, #0a0d12 88%); }
  .book-title { position: absolute; left: 0; width: 100%; top: 62px; text-align: center; font-family: "Oswald", Impact, sans-serif; font-weight: 700; font-size: 54px; line-height: 1; color: var(--title-yellow); letter-spacing: -0.5px; }
  .book-subtitle { position: absolute; left: 0; width: 100%; top: 131px; text-align: center; color: var(--text-white); font-weight: 700; font-size: 18.5px; }
  .cover-art { position: absolute; left: 35px; top: 188px; width: 430px; height: 460px; border-radius: 50%;
    background: radial-gradient(ellipse at 55% 55%, rgba(230,70,50,0.55) 0%, rgba(150,200,215,0.35) 45%, rgba(40,100,125,0) 75%); }
  .front-author { position: absolute; right: 40px; top: 738px; color: var(--text-white); font-weight: 700; font-size: 15px; }
</style>
</head>
<body>
<div class="sheet">
  <div class="color-bar"><span class="c">CYAN</span> <span class="m">MAGENTA</span> <span class="y">YELLOW</span> <span class="k">BLACK</span></div>

  <section class="back-cover">
    <div class="publisher-mark"><span class="dot"></span>MARLOW GROUP</div>
    <div class="isbn-box">ISBN No.</div>
  </section>

  <section class="spine">
    <div class="spine-text">
      <span class="spine-title">The Sideline Launch</span>
      <span class="spine-subtitle">Growing a Venture Around Your Day Job</span>
      <span class="spine-author">Author R. K. Holloway</span>
    </div>
  </section>

  <section class="front-cover">
    <h1 class="book-title">The Sideline Launch</h1>
    <p class="book-subtitle">Growing a Venture Around Your Day Job</p>
    <div class="cover-art" role="img" aria-label="Illustration: a white 3D figure shrugging beside a large red question mark, surrounded by chalk sketches of arrows, a light bulb and a thought cloud"></div>
    <p class="front-author">Author R. K. Holloway</p>
  </section>

  <svg class="trim-marks" width="1200" height="900" viewBox="0 0 1200 900">
    <g stroke="#000" stroke-width="0.6">
      <line x1="64" y1="0" x2="64" y2="57"/>
      <line x1="578.5" y1="0" x2="578.5" y2="57"/>
      <line x1="621.5" y1="0" x2="621.5" y2="57"/>
      <line x1="1135" y1="0" x2="1135" y2="57"/>
      <line x1="64" y1="842" x2="64" y2="900"/>
      <line x1="578.5" y1="842" x2="578.5" y2="900"/>
      <line x1="621.5" y1="842" x2="621.5" y2="900"/>
      <line x1="1135" y1="842" x2="1135" y2="900"/>
      <line x1="0" y1="64" x2="57" y2="64"/>
      <line x1="1143" y1="64" x2="1200" y2="64"/>
      <line x1="0" y1="835" x2="57" y2="835"/>
      <line x1="1143" y1="835" x2="1200" y2="835"/>
    </g>
  </svg>

  <svg class="reg-marks" width="1200" height="900" viewBox="0 0 1200 900">
    <defs>
      <g id="reg">
        <circle r="8" fill="none" stroke="#000" stroke-width="0.8"/>
        <circle r="4.5" fill="#000"/>
        <line x1="-12" y1="0" x2="12" y2="0" stroke="#000" stroke-width="0.8"/>
        <line x1="0" y1="-12" x2="0" y2="12" stroke="#000" stroke-width="0.8"/>
      </g>
    </defs>
    <use href="#reg" x="43" y="43"/>
    <use href="#reg" x="1157" y="43"/>
    <use href="#reg" x="43" y="857"/>
    <use href="#reg" x="1157" y="857"/>
  </svg>
</div>
</body>
</html>
```